Web Design Project

I need designs (PSD only - no programming) for several pages of a new website helping train operators to manage key information about their traindrivers.
The main feature of this website is the management of personnel records (create, edit, search, delete). Another key aspect is the management of user privileges. Since this is a new website we also need a user friendly frontpage, pricing information and how it works sections.
This can be broken down into 9 pages for which we need designs (PSDs).
1. Home
2. Driver record
3. How it works
4. Pricing
5. User administration
6. Help
7. Record list view
8. Login
9. Registration
Navigation (not logged in) are: Home | How it works | Pricing | Customers | About us | Contact
Navigation (logged in) are: Overview | Administration | Manage records | Billing | Help | Contact
Footer: Customer logos | Awards | Terms & Conditions | Privacy
To provide the best support for you to come up with a strong design proposal I will provide DAILY feedback to all participants. We have also created concept mockups (attached) and example pages (below) for each section to give you a clear sense of what we look for.
The core concepts for a successful bid are that the website is EASY to understand, INTUITIVE to navigate, and SIMPLE to use. Most of our users lack technical background and are looking for tool to simplify their work.
The strongest participants (winner and close contenders) will have the opportunity to additional commissioned work on additional sections not included in this brief.
Example Pages (by section)
1. http://www.brovendale.example/site-keepers/
1. http://www.qvt.example/
1. http://www.mondaph.example/
1. http://www.gorvanquest.example/
2. http://www.snapveld.example/profile_edit.gne
3. https://www.tarn.example/how-it-works/
3. http://www.bulkvue.example/learn
4. http://www.pactheron.example/crm/editions-pricing.jsp
4. http://www.brovendale.example/site-keepers/prices
6. https://support.talvora.example/en-gb/
6. http://help.dealmeadow.example/contact_us
8. https://www.careweave.example/uas/login
8. https://www.dealmeadow.example/login
8. http://www.askhollow.example/login/index
For form designs we like Verindo, Bidnook, Snapveld, CareWeave, Chatterly and the concepts presented by Tomas Kerrigan in his classic Layout Craft Shaping the Input Boxes.
For additional guidance see mockups attached!
Target Market(s)
Security, human resources and admin support employees for train operators.
Industry/Entity Type
Learn
Requirements
Should not have
- Home page should not have
Social media icons (chatterly, chirpla, CareWeave, RSS feed)
Contact forms
Read more links
Old trains

```html
<!DOCTYPE html>
<html lang="en">
<head>
<meta charset="utf-8">
<title>Tracklane – Pricing &amp; Packages</title>
<link href="https://fonts.googleapis.com/css2?family=Open+Sans:wght@400;600&family=Oswald:wght@600&family=Roboto:wght@400;700&family=Playfair+Display:ital,wght@1,700;1,900&display=swap" rel="stylesheet">
<style>
:root{
  --brand:#e8705f;
  --brand-deep:#d9412e;
  --brand-dark:#5a1f17;
  --page:#f4f4f4;
  --card-frame:#dcdcdc;
  --text:#555;
  --muted:#999;
  --white:#fff;
}
*{margin:0;padding:0;box-sizing:border-box}
html,body{width:1200px;height:1077px;overflow:hidden}
body{position:relative;background:var(--page);font-family:"Open Sans",sans-serif;color:var(--text)}
.abs{position:absolute}
.header{left:0;top:0;width:1200px;height:249px;background:var(--brand)}
.brand{left:204px;top:28px;display:flex;align-items:center;gap:10px;font-family:"Oswald",sans-serif;font-weight:600;font-size:34px;color:var(--white);letter-spacing:.5px}
.brand-mark{width:36px;height:36px;border-radius:50%;background:var(--brand-dark)}
.utility{top:8px;left:757px;font-size:13px;color:var(--white);display:flex;gap:8px;align-items:center}
.utility .lang{margin-left:30px}
.lang-select{border:1px solid var(--white);font-size:10px;padding:1px 6px;display:flex;gap:8px;align-items:center}
.main-nav{left:346px;top:92px;display:flex;font-size:17px;color:var(--white)}
.main-nav span{display:block;padding:0 25px;position:relative;height:32px}
.main-nav .active::after{content:"";position:absolute;left:0;right:0;bottom:-1px;height:6px;background:var(--white)}
.nav-rule{left:171px;top:124px;width:857px;height:3px;background:var(--white)}
.tagline{left:0;width:1200px;top:143px;text-align:center;font-family:"Roboto",sans-serif;font-weight:700;font-size:27px;line-height:31px;color:var(--white)}
.page-title{left:178px;top:258px;font-weight:600;font-size:68px;color:var(--brand-deep);letter-spacing:-.5px}
.intro{left:181px;top:376px;width:430px;font-family:"Roboto",sans-serif;font-size:11px;line-height:17px;color:var(--text)}
.cta{height:47px;background:var(--brand-deep);color:var(--white);font-family:"Roboto",sans-serif;font-weight:700;font-size:31px;text-align:center;line-height:46px;box-shadow:0 10px 8px -8px rgba(0,0,0,.45)}
.cta-top{left:634px;top:369px;width:365px}
.cta-bottom{left:421px;top:825px;width:365px}
.card{top:452px;width:235px;height:276px;background:var(--card-frame);border:1px solid #ccc}
.card-inner{position:absolute;left:9px;top:9px;right:9px;bottom:10px;background:var(--white)}
.card h2{font-family:"Playfair Display",serif;font-style:italic;font-weight:700;font-size:28px;color:var(--brand);text-align:center;margin:6px 8px 0;padding-bottom:2px;border-bottom:1px solid #ddd}
.card ul{list-style:none;margin:13px 0 0 16px;font-family:"Roboto",sans-serif;font-size:11px;line-height:19.6px;color:var(--text)}
.card li::before{content:"";display:inline-block;width:4px;height:4px;border-radius:50%;background:#bbb;margin-right:8px;vertical-align:middle}
.price{position:absolute;left:0;right:0;top:168px;height:42px;line-height:42px;text-align:center;font-family:"Playfair Display",serif;font-style:italic;font-weight:900;color:#111;white-space:nowrap}
.price .only{font-size:15px}
.price .amount{font-size:38px;margin:0 6px}
.price .cents{font-size:14px;position:relative;top:-6px}
.buy{position:absolute;left:31px;top:246px;width:170px;height:57px;background:var(--brand-deep);border:1px solid #b83322;border-radius:2px;color:var(--white);font-family:"Playfair Display",serif;font-style:italic;font-weight:700;font-size:27px;text-align:center;line-height:55px}
.rule{left:186px;width:834px;height:1px;background:#ddd}
.logo-strip{left:186px;top:925px;width:834px;display:flex;justify-content:space-around;align-items:center;font-size:20px;font-weight:600;color:#a8a8a8}
.logo-strip span{display:flex;align-items:center;gap:6px}
.logo-strip i{display:inline-block;width:18px;height:18px;border-radius:50%;background:#c8c8c8}
.to-top{left:996px;top:992px;width:32px;height:30px;background:var(--brand-deep)}
.footer-bar{left:171px;top:1017px;width:857px;height:5px;background:var(--brand-deep)}
.copyright{left:187px;top:1036px;font-size:10px;color:var(--brand-deep)}
.footer-nav{right:187px;top:1033px;display:flex;gap:38px;font-size:12px;color:var(--brand-deep)}
.contact-tab{left:0;top:601px;width:46px;height:222px;background:var(--brand-deep);display:flex;align-items:center;justify-content:center}
.contact-tab span{transform:rotate(-90deg);white-space:nowrap;font-family:"Open Sans",sans-serif;font-weight:600;font-size:33px;color:var(--white)}
</style>
</head>
<body>
<header class="abs header"></header>
<div class="abs brand"><span class="brand-mark"></span>TRACKLANE</div>
<div class="abs utility"><span>register</span><span>|</span><span>login</span><span class="lang">language</span><span class="lang-select">english
  <svg width="7" height="4" viewBox="0 0 7 4"><path d="M0 0h7L3.5 4z" fill="#fff"/></svg></span></div>
<nav class="abs main-nav"><span class="active">home</span><span>how it work</span><span>pricing</span><span>our customers</span><span>about us</span><span>contact</span></nav>
<div class="abs nav-rule"></div>
<p class="abs tagline">We provide management of personnel records<br>(create, edit, search, delete).</p>

<h1 class="abs page-title">Pricing &amp; Packages</h1>
<p class="abs intro">Lorem ipsum dolor sit amet. Text blurb for pricing &amp; Packages explanation will come here. This should be small 2-3 sentence desciption to carry the looks.</p>
<div class="abs cta cta-top">Sign up or request a call</div>

<section class="abs card" style="left:195px"><div class="card-inner"><h2>Express</h2>
<ul><li>Mauris sed massa massa.</li><li>Eu condimentum nisl.</li><li>Ut enim leo, rhoncus nec.</li><li>Elementum vitae, sagittis ac tortor.</li></ul>
<div class="price"><span class="only">Only</span><span class="amount">$29</span><span class="cents">.99</span></div></div>
<div class="buy">Buy Now!!!</div></section>

<section class="abs card" style="left:480px"><div class="card-inner"><h2>Standard</h2>
<ul><li>Mauris sed massa massa.</li><li>Eu condimentum nisl.</li><li>Ut enim leo, rhoncus nec.</li><li>Elementum vitae, sagittis ac tortor.</li></ul>
<div class="price"><span class="only">Only</span><span class="amount">$39</span><span class="cents">.99</span></div></div>
<div class="buy">Buy Now!!!</div></section>

<section class="abs card" style="left:765px"><div class="card-inner"><h2>Professional</h2>
<ul><li>Mauris sed massa massa.</li><li>Eu condimentum nisl.</li><li>Ut enim leo, rhoncus nec.</li><li>Elementum vitae, sagittis ac tortor.</li></ul>
<div class="price"><span class="only">Only</span><span class="amount">$69</span><span class="cents">.99</span></div></div>
<div class="buy">Buy Now!!!</div></section>

<div class="abs rule" style="top:789px"></div>
<div class="abs cta cta-bottom">Sign up or request a call</div>

<div class="abs rule" style="top:912px;background:#f0c8c0"></div>
<div class="abs logo-strip"><span><i></i>Novaline</span><span><i></i>Pillaro</span><span>Wendel</span><span><i></i>Meridiana</span><span><i></i>Brightway</span><span><i></i>Quillmont</span></div>
<div class="abs rule" style="top:972px;background:#f0c8c0"></div>

<div class="abs to-top"><svg width="32" height="30" viewBox="0 0 32 30"><path d="M9 19l7-7 7 7" fill="none" stroke="#fff" stroke-width="3"/></svg></div>
<div class="abs footer-bar"></div>
<p class="abs copyright">copyright2@ tracklane2012</p>
<nav class="abs footer-nav"><span>home</span><span>how it work</span><span>pricing</span><span>our customers</span><span>about us</span><span>contact</span></nav>

<div class="abs contact-tab"><span>Contact us</span></div>
</body>
</html>
```